Bright Harbour Mortgages Social Media Campaign

I need social media campaign banners. Facebook and Instagram.
I would like them to incorporate local photos, my photo and my logo. I have some sample files of previous campaigns and I have a color scheme associated with my brand. My business operates in St. John's Newfoundland.

Target Market(s)

Home Buyers, Home Owners

Industry/Entity Type

Mortgage Brokering

Logo Text

Bright Harbour Mortgages

Logo styles of interest
Lettermark Logo
Font styles to use
Other font styles liked:
• Times New Roman, I'm open to suggestion

Colors
0054AA
0677BA
7BADD7
CADEEF
E8F1F8
EE7325
F08F49
F5BC92
FAE3D3
FDF4ED

Requirements
Must have
• My name, photo, contact info, slogan
Nice to have
• We can discuss slogans to use, I can provide some suggestions.

```html
<!DOCTYPE html>
<html lang="en">
<head>
<meta charset="utf-8">
<title>Bright Harbour Mortgages – Social Banner</title>
<link rel="stylesheet" href="https://fonts.googleapis.com/css2?family=Montserrat:wght@400;500;700;800&display=swap">
<style>
  :root{
    --navy:#0b1852;
    --orange:#ff4200;
    --amber:#ff9300;
    --white:#ffffff;
    --button-top:#1a5fe0;
    --button-bottom:#0a2f8c;
    --sky-top:#0a5ad4;
    --sky-bottom:#8fbbe8;
    --portrait-fill:#a9b4c8;
  }
  *{margin:0;padding:0;box-sizing:border-box}
  html,body{width:1200px;height:1200px;overflow:hidden;background:var(--white)}
  .banner{position:relative;width:1200px;height:1200px;overflow:hidden;font-family:'Montserrat',sans-serif;background:var(--navy)}
  .shapes{position:absolute;inset:0}
  .brand{position:absolute;left:58px;top:130px;display:flex;align-items:center;gap:14px}
  .brand-mark{width:22px;height:22px;background:var(--orange);flex:none}
  .brand-name{font-weight:800;font-size:28px;color:var(--orange);white-space:nowrap}
  .headline{position:absolute;left:74px;top:436px;color:var(--white);font-weight:800;font-size:54px;line-height:68px;text-transform:uppercase;letter-spacing:-0.3px}
  .subline{position:absolute;left:72px;top:580px;color:var(--white);font-weight:400;font-size:33px;line-height:47px;white-space:nowrap}
  .subline strong{font-weight:700}
  .cta{position:absolute;left:70px;top:694px;width:246px;height:54px;border-radius:4px;background:linear-gradient(var(--button-top),var(--button-bottom));color:var(--white);font-weight:500;font-size:30px;display:flex;align-items:center;justify-content:center;gap:6px;box-shadow:0 2px 3px rgba(0,0,0,.3)}
  .cta-arrows{color:var(--orange);font-weight:800}
  .contact{position:absolute;left:64px;top:922px;color:var(--white)}
  .contact-call{color:var(--orange);font-weight:800;font-size:40px}
  .contact-phone{display:flex;align-items:center;gap:18px;margin-top:2px;font-weight:800;font-size:64px;letter-spacing:-0.5px;white-space:nowrap}
  .contact-line{display:flex;align-items:center;gap:14px;font-size:32px;font-weight:500;margin-top:8px;white-space:nowrap}
  .contact-line .accent{color:var(--orange)}
  .icon-ring{width:42px;height:42px;border:2px solid var(--white);border-radius:50%;display:flex;align-items:center;justify-content:center;flex:none}
</style>
</head>
<body>
<main class="banner">
  <svg class="shapes" width="1200" height="1200" viewBox="0 0 1200 1200">
    <defs>
      <linearGradient id="sky" x1="0" y1="0" x2="0" y2="1">
        <stop offset="0" stop-color="var(--sky-top)"/>
        <stop offset="1" stop-color="var(--sky-bottom)"/>
      </linearGradient>
    </defs>
    <polygon class="local-photo" role="img" aria-label="Photo of a historic stone tower on a hill under a blue sky in St. John's" points="802,0 1200,0 1200,516 775,736 323,283" fill="url(#sky)"/>
    <polygon class="panel-white" points="0,0 802,0 323,283 0,375" fill="var(--white)"/>
    <polygon class="panel-orange" points="0,375 323,283 775,643 775,736 208,885 0,758" fill="var(--orange)"/>
    <polygon class="accent-amber" points="1048,595 1200,512 1200,907 1048,843" fill="var(--amber)"/>
    <rect class="agent-photo" role="img" aria-label="Portrait photo of the mortgage broker" x="620" y="400" width="565" height="800" fill="var(--portrait-fill)"/>
  </svg>

  <header class="brand">
    <span class="brand-mark"></span>
    <span class="brand-name">BRIGHT HARBOUR MORTGAGES</span>
  </header>

  <h1 class="headline">We Think<br>Outside The Box</h1>
  <p class="subline">We Get <strong>The Lowest Rates</strong> and<br>Best Deals <strong>For Our Clients</strong></p>
  <div class="cta">Get Started <span class="cta-arrows">»</span></div>

  <section class="contact">
    <div class="contact-call">Call Marissa:</div>
    <div class="contact-phone">
      <svg width="40" height="40" viewBox="0 0 24 24" aria-hidden="true"><path fill="#fff" d="M6.6 10.8a15 15 0 0 0 6.6 6.6l2.2-2.2c.3-.3.7-.4 1-.2 1.1.4 2.3.6 3.6.6.6 0 1 .4 1 1V20c0 .6-.4 1-1 1A17 17 0 0 1 3 4c0-.6.4-1 1-1h3.5c.6 0 1 .4 1 1 0 1.3.2 2.5.6 3.6.1.3 0 .7-.2 1z"/><path fill="none" stroke="#fff" stroke-width="1.8" d="M14 3a7 7 0 0 1 7 7M14 6.5a3.5 3.5 0 0 1 3.5 3.5"/></svg>
      709-555-0142
    </div>
    <div class="contact-line">
      <span class="icon-ring"><svg width="22" height="22" viewBox="0 0 24 24" aria-hidden="true"><g fill="none" stroke="var(--orange)" stroke-width="2"><circle cx="12" cy="12" r="9"/><ellipse cx="12" cy="12" rx="4" ry="9"/><path d="M3 12h18M5 7h14M5 17h14"/></g></svg></span>
      <span>www.<span class="accent">capelinmortgages</span>.com</span>
    </div>
    <div class="contact-line">
      <span class="icon-ring"><svg width="22" height="22" viewBox="0 0 24 24" aria-hidden="true"><rect x="3" y="6" width="18" height="13" fill="var(--orange)"/><path d="M3 6l9 7 9-7" fill="none" stroke="var(--navy)" stroke-width="1.6"/></svg></span>
      <span>info@<span class="accent">capelinmortgages</span>.com</span>
    </div>
  </section>
</main>
</body>
</html>
```